Larkspur Ridge Management - Business Cards

I need business cards. My current logo was designed by a designer at this site and I very much like and am happy with the results. I would like a business card that is trendy, unique, current yet professional. I deal with high net worth clients daily

Target Market(s)

Out of state investors looking to get into the rental market in Ohio

Industry/Entity Type

Property Management, Consulting

Contact Information for Business Card

Name, Title (Chief Financial Officer) office phone number (555) 817-3094 website address larkridgemgmt.example

Font styles to use
Sans Serif

Colors
0054AA
0677BA
7BADD7
CADEEF
E8F1F8
0094D4
00A9DD
6FCCEA
C7EBF8
E9F6FB
00AB8E
00BBA5
67D7C9
C6EFE9
E9F9F6

```html
<!DOCTYPE html>
<html lang="en">
<head>
<meta charset="utf-8">
<title>Larkspur Ridge Management – Business Cards</title>
<link href="https://fonts.googleapis.com/css2?family=Montserrat:wght@500;600;700;800&display=swap" rel="stylesheet">
<style>
  :root {
    --navy: #233457;
    --red: #c8242c;
    --white: #ffffff;
    --paper: #ffffff;
    --city-dark: #0f1d1f;
    --city-mid: #2a3a3a;
    --city-warm: #5a4a3a;
  }
  * { box-sizing: border-box; margin: 0; padding: 0; }
  html, body { width: 1200px; height: 1200px; overflow: hidden; background: var(--paper); }
  body { position: relative; font-family: "Montserrat", sans-serif; }

  .card { position: absolute; width: 569px; height: 342px; overflow: hidden; }

  /* Front */
  .card-front { left: 181px; top: 253px; background: var(--navy); }
  .front-brand {
    position: absolute; left: 0; right: 0; top: 112px;
    text-align: center; color: var(--white); font-weight: 800;
    line-height: 1.05;
  }
  .front-brand .brand-line-main { display: block; font-size: 40px; letter-spacing: 1px; }
  .front-brand .brand-line-sub { display: block; font-size: 20px; letter-spacing: 4px; margin-top: 8px; }
  .tagline {
    position: absolute; left: 0; right: 0; top: 299px;
    display: flex; justify-content: center; gap: 26px;
    font-size: 17px; font-weight: 500; letter-spacing: 4.5px; color: var(--white);
  }
  .tagline .divider { color: var(--red); letter-spacing: 0; }

  /* Back */
  .card-back { left: 457px; top: 612px; background: var(--white); border: 1px solid #cfd3da; }
  .chevron-art { position: absolute; inset: 0; }
  .holder-name {
    position: absolute; left: 66px; top: 42px;
    font-size: 30px; font-weight: 800; color: var(--navy); letter-spacing: 0.5px;
  }
  .holder-title {
    position: absolute; left: 64px; top: 78px;
    font-size: 16px; font-weight: 600; color: var(--red);
  }
  .contact-row {
    position: absolute; left: 64px; display: flex; align-items: center; gap: 12px;
    font-size: 14.5px; font-weight: 600; color: var(--navy); letter-spacing: 0.2px;
    white-space: nowrap;
  }
  .contact-phone { top: 144px; }
  .contact-web { top: 191px; }
  .contact-icon { width: 34px; height: 34px; flex: none; }
  .rule { position: absolute; left: 42px; top: 298px; width: 262px; height: 1.5px; background: var(--red); }
  .services {
    position: absolute; left: 42px; top: 318px;
    display: flex; gap: 15px;
    font-size: 9px; font-weight: 600; letter-spacing: 2.6px; color: var(--navy);
  }
  .services .divider { color: var(--red); letter-spacing: 0; }
  .back-brand {
    position: absolute; left: 432px; top: 252px; width: 108px;
    text-align: center; color: var(--white); font-size: 12px; font-weight: 700; line-height: 1.2;
  }
</style>
</head>
<body>

<section class="card card-front" aria-label="Business card front">
  <div class="front-brand">
    <span class="brand-line-main">LARKSPUR RIDGE</span>
    <span class="brand-line-sub">MANAGEMENT</span>
  </div>
  <div class="tagline">
    <span>MANAGE</span><span class="divider">|</span>
    <span>MAXIMIZE</span><span class="divider">|</span>
    <span>GROW</span>
  </div>
</section>

<section class="card card-back" aria-label="Business card back">
  <svg class="chevron-art" viewBox="0 0 569 342" width="569" height="342">
    <defs>
      <linearGradient id="cityTone" x1="0" y1="0" x2="0" y2="1">
        <stop offset="0" stop-color="var(--city-dark)"/>
        <stop offset="0.6" stop-color="var(--city-mid)"/>
        <stop offset="1" stop-color="var(--city-warm)"/>
      </linearGradient>
    </defs>
    <polyline points="406,0 284,169 406,342" fill="none" stroke="var(--navy)" stroke-width="3"/>
    <polygon points="414,0 294,169 414,342 569,342 569,0" fill="var(--red)"/>
    <polygon points="441,0 318,169 441,342 569,342 569,0" fill="url(#cityTone)"
             role="img" aria-label="Night skyline photograph of city towers by the water"/>
  </svg>

  <h1 class="holder-name">YOUR NAME</h1>
  <p class="holder-title">CHIEF FINANCIAL OFFICER</p>

  <div class="contact-row contact-phone">
    <svg class="contact-icon" viewBox="0 0 36 36" aria-hidden="true">
      <circle cx="18" cy="18" r="18" fill="var(--navy)"/>
      <path d="M12.5 10.5c1-.8 2-.6 2.6.3l1.5 2.3c.5.8.3 1.7-.4 2.2l-1 .8c.8 2 2.6 3.9 4.6 4.8l.8-1c.6-.7 1.5-.9 2.3-.4l2.3 1.5c.9.6 1 1.7.2 2.6l-1.2 1.3c-1 1-2.6 1.2-4 .5-3.9-1.9-7-5-8.8-8.9-.6-1.4-.4-3 .7-4z" fill="var(--white)"/>
    </svg>
    <span>(555) 817-3094</span>
  </div>

  <div class="contact-row contact-web">
    <svg class="contact-icon" viewBox="0 0 36 36" aria-hidden="true" fill="none" stroke="var(--navy)" stroke-width="2.2">
      <circle cx="18" cy="18" r="15.5"/>
      <ellipse cx="18" cy="18" rx="7" ry="15.5"/>
      <line x1="18" y1="2.5" x2="18" y2="33.5"/>
      <line x1="2.5" y1="18" x2="33.5" y2="18"/>
      <path d="M5 10.5h26M5 25.5h26"/>
    </svg>
    <span>larkridgemgmt.example</span>
  </div>

  <div class="rule"></div>
  <div class="services">
    <span>PROPERTY MANAGEMENT</span><span class="divider">|</span><span>CONSULTING</span>
  </div>

  <div class="back-brand">LARKSPUR RIDGE MANAGEMENT</div>
</section>

</body>
</html>
```